Sports Photography Business Cards

I recently started a small photography business, mainly school sports photography. I already have a logo, but I am looking for business cards to get more people to my website and be able to contact me easily. I also have a QR code (which brings you to my site) that I would like to include on the card. I want to include my phone number, email, Instagram link, and website address.
I love the colors green and pink, but I am not 100% committed to any. I would love to have foil on my cards, but it is not a deal breaker.
The final design should be clean, easy to read, and eye catching.
Target Market(s)
Parents
Industry/Entity Type
Photography
Contact Information for Business Card
Phone Number, Email, Website, QR Code
Look and feel
Each slider illustrates characteristics of the customer's brand and the style your logo design should communicate.

```html
<!DOCTYPE html>
<html lang="en">
<head>
<meta charset="UTF-8">
<title>Maren Holt Photography – Business Cards</title>
<link rel="stylesheet" href="https://fonts.googleapis.com/css2?family=Arimo:wght@400;700&family=Josefin+Sans:wght@300&display=swap">
<style>
  :root {
    --backdrop: #2a2a2a;
    --card: #0b0b0b;
    --ink: #ffffff;
    --rule: #5a5a5a;
  }
  * { margin: 0; padding: 0; box-sizing: border-box; }
  html, body {
    width: 1200px; height: 900px; overflow: hidden;
    background: var(--backdrop);
  }
  .sheet {
    width: 1200px; height: 900px;
    display: flex; align-items: center; justify-content: center; gap: 40px;
  }
  .card {
    position: relative;
    width: 540px; height: 309px;
    background: var(--card);
    color: var(--ink);
    border-radius: 2px;
    overflow: hidden;
  }

  /* Front: mark + contact */
  .card--front { display: flex; align-items: center; }
  .mark {
    flex: 0 0 auto;
    width: 170px; height: 170px;
    margin-left: 48px;
    border: 3px solid var(--ink);
    border-radius: 50%;
    display: flex; align-items: center; justify-content: center;
    font-family: "Arimo", sans-serif; font-weight: 400;
    font-size: 22px; text-align: center; line-height: 1.2;
  }
  .divider {
    width: 1px; height: 150px;
    background: var(--rule);
    margin: 0 30px 0 40px;
  }
  .contact { font-family: "Arimo", sans-serif; }
  .contact__name { font-size: 23px; font-weight: 400; line-height: 1.05; }
  .contact__role { font-size: 15px; margin-bottom: 14px; }
  .contact__list { list-style: none; font-size: 15px; line-height: 1.45; }
  .contact__list li { display: flex; align-items: center; gap: 8px; }
  .contact__list li.social { margin-top: 8px; }
  .contact__list svg { width: 14px; height: 14px; flex: 0 0 auto; }
  .dot {
    width: 12px; height: 12px; border: 1.5px solid var(--ink);
    border-radius: 50%; flex: 0 0 auto; margin: 0 1px;
  }

  /* Back: brand lockup */
  .card--back {
    display: flex; flex-direction: column; align-items: center; justify-content: center;
  }
  .brand-mark {
    width: 120px; height: 120px;
    border: 2px solid var(--ink); border-radius: 50%;
    margin-bottom: 22px;
  }
  .brand-name {
    font-family: "Arimo", sans-serif; font-weight: 400;
    font-size: 30px; letter-spacing: 1px; margin-bottom: 10px;
  }
  .brand-trade {
    font-family: "Josefin Sans", sans-serif; font-weight: 300;
    font-size: 22px; letter-spacing: 2px;
  }
</style>
</head>
<body>
<main class="sheet">

  <section class="card card--front" aria-label="Business card front">
    <div class="mark">Maren<br>Holt</div>
    <div class="divider"></div>
    <div class="contact">
      <h1 class="contact__name">Maren Holt</h1>
      <p class="contact__role">Photography</p>
      <ul class="contact__list">
        <li>
          <svg viewBox="0 0 16 16" aria-hidden="true"><path d="M3 1.5l2.6 0.4 1 3-1.6 1.3a9 9 0 0 0 4.8 4.8l1.3-1.6 3 1 .4 2.6-1.8 1.6C7.4 14.2 1.8 8.6 1.4 3.3z" fill="#fff"/></svg>
          044-555 210 347
        </li>
        <li>
          <svg viewBox="0 0 16 16" aria-hidden="true"><rect x="1" y="3" width="14" height="10" fill="#fff"/><path d="M1 3l7 6 7-6" fill="none" stroke="#0b0b0b" stroke-width="1.4"/></svg>
          info@holtframes.com
        </li>
        <li>
          <svg viewBox="0 0 16 16" aria-hidden="true"><g fill="none" stroke="#fff" stroke-width="1.3"><circle cx="8" cy="8" r="6.5"/><ellipse cx="8" cy="8" rx="2.8" ry="6.5"/><path d="M1.5 8h13M2.5 4.8h11M2.5 11.2h11"/></g></svg>
          www.holtframes.com
        </li>
        <li class="social">
          <span class="dot" aria-hidden="true"></span>
          @marenholtphoto
        </li>
      </ul>
    </div>
  </section>

  <section class="card card--back" aria-label="Business card back">
    <div class="brand-mark" aria-hidden="true"></div>
    <p class="brand-name">Maren Holt</p>
    <p class="brand-trade">PHOTOGRAPHY</p>
  </section>

</main>
</body>
</html>
```